Sign listing benefits of Wash and Fold Service

Sign 48 inches wide and 24 inches height to showcase service listed above.
Benefits include:
Saves Money
Saves Time
Convenient
Stain Treatment

Looking for something colorful (Blue and white are our business colors) the look of a laundromat business.

```html
<!DOCTYPE html>
<html lang="en">
<head>
<meta charset="utf-8">
<title>Wash and Fold Service Sign</title>
<link rel="stylesheet" href="https://fonts.googleapis.com/css2?family=Montserrat:wght@700;800;900&family=Pacifico&display=swap">
<style>
  :root {
    --page-bg: #e6e6e6;
    --navy: #062477;
    --deep-blue: #0a3a9a;
    --teal-glow: #00b3d6;
    --cyan-band: #00ccff;
    --pale-cyan: #c9fdff;
    --white: #ffffff;
    --ink-blue: #0b2a7a;
    --orange-light: #f29a00;
    --orange: #ff6a00;
    --photo-light: #f4f1ec;
    --photo-mid: #cfd9ea;
    --photo-warm: #c9b89c;
  }
  html, body {
    margin: 0;
    width: 1200px;
    height: 1200px;
    overflow: hidden;
    background: var(--page-bg);
  }
  .sign {
    position: absolute;
    left: 40px;
    top: 320px;
    width: 1120px;
    height: 559px;
    display: block;
  }
  .title {
    font-family: "Montserrat", sans-serif;
    font-weight: 900;
    font-size: 128px;
    fill: var(--white);
  }
  .title-shadow { fill: var(--navy); }
  .script {
    font-family: "Pacifico", cursive;
    font-size: 100px;
    fill: var(--white);
  }
  .script-shadow { fill: var(--navy); }
  .pill-label {
    font-family: "Montserrat", sans-serif;
    font-weight: 800;
    font-size: 50px;
    fill: var(--white);
  }
  .benefit {
    font-family: "Montserrat", sans-serif;
    font-weight: 800;
    font-size: 54px;
    fill: var(--ink-blue);
  }
</style>
</head>
<body>
<svg class="sign" viewBox="0 0 1668 832" xmlns="http://www.w3.org/2000/svg">
  <defs>
    <radialGradient id="skyGlow" cx="0.52" cy="0.3" r="0.45">
      <stop offset="0" stop-color="var(--teal-glow)"/>
      <stop offset="0.55" stop-color="var(--deep-blue)"/>
      <stop offset="1" stop-color="var(--navy)"/>
    </radialGradient>
    <linearGradient id="pillFill" x1="0" y1="0" x2="1" y2="1">
      <stop offset="0" stop-color="var(--orange-light)"/>
      <stop offset="0.6" stop-color="var(--orange)"/>
    </linearGradient>
    <linearGradient id="tickFill" x1="0" y1="0" x2="0" y2="1">
      <stop offset="0" stop-color="var(--orange-light)"/>
      <stop offset="1" stop-color="var(--orange)"/>
    </linearGradient>
    <linearGradient id="photoTones" x1="0" y1="0" x2="1" y2="1">
      <stop offset="0" stop-color="var(--photo-light)"/>
      <stop offset="0.55" stop-color="var(--photo-mid)"/>
      <stop offset="1" stop-color="var(--photo-warm)"/>
    </linearGradient>
  </defs>

  <!-- background layers -->
  <rect class="sky" width="1668" height="832" fill="url(#skyGlow)"/>
  <path class="wave-band" d="M0 330 C200 300 420 290 620 350 C820 410 1000 420 1200 350 C1360 300 1500 250 1668 262 L1668 832 L0 832 Z" fill="var(--cyan-band)"/>
  <path class="wave-pale" d="M0 372 C200 340 420 345 620 390 C820 435 1000 440 1200 385 C1360 345 1520 300 1668 305 L1668 832 L0 832 Z" fill="var(--pale-cyan)"/>

  <!-- photo area -->
  <path class="photo" role="img" aria-label="Photo of a smiling woman holding a stack of fresh folded white and blue towels over a wicker laundry basket"
        d="M0 440 C60 420 130 300 160 170 C190 110 330 100 380 170 C410 230 420 300 440 345 L660 345 C700 380 710 430 700 500 L860 640 L830 832 L0 832 Z"
        fill="url(#photoTones)"/>

  <!-- headline -->
  <text class="title title-shadow" x="499" y="153">Wash and Fold</text>
  <text class="title" x="493" y="147">Wash and Fold</text>
  <text class="script script-shadow" x="612" y="291">Service</text>
  <text class="script" x="606" y="285">Service</text>

  <!-- benefits heading pill -->
  <rect class="pill-border" x="904" y="336" width="628" height="118" rx="59" fill="var(--white)"/>
  <rect class="pill" x="912" y="344" width="612" height="102" rx="51" fill="url(#pillFill)"/>
  <text class="pill-label" x="1218" y="413" text-anchor="middle">Benefits include:</text>

  <!-- benefit list -->
  <g class="benefit-list">
    <g class="benefit-item" transform="translate(940 484)">
      <circle r="30" fill="var(--white)"/><circle r="26" fill="url(#tickFill)"/>
      <path d="M-12 0 L-3 10 L13 -9" fill="none" stroke="var(--white)" stroke-width="7" stroke-linecap="round" stroke-linejoin="round"/>
    </g>
    <text class="benefit" x="994" y="504">Saves Money</text>

    <g class="benefit-item" transform="translate(940 593)">
      <circle r="30" fill="var(--white)"/><circle r="26" fill="url(#tickFill)"/>
      <path d="M-12 0 L-3 10 L13 -9" fill="none" stroke="var(--white)" stroke-width="7" stroke-linecap="round" stroke-linejoin="round"/>
    </g>
    <text class="benefit" x="994" y="613">Saves Time</text>

    <g class="benefit-item" transform="translate(940 672)">
      <circle r="30" fill="var(--white)"/><circle r="26" fill="url(#tickFill)"/>
      <path d="M-12 0 L-3 10 L13 -9" fill="none" stroke="var(--white)" stroke-width="7" stroke-linecap="round" stroke-linejoin="round"/>
    </g>
    <text class="benefit" x="994" y="692">Convenient</text>

    <g class="benefit-item" transform="translate(940 752)">
      <circle r="30" fill="var(--white)"/><circle r="26" fill="url(#tickFill)"/>
      <path d="M-12 0 L-3 10 L13 -9" fill="none" stroke="var(--white)" stroke-width="7" stroke-linecap="round" stroke-linejoin="round"/>
    </g>
    <text class="benefit" x="994" y="772">Stain Treatment</text>
  </g>
</svg>
</body>
</html>
```